Corvale Holdings Business Cards

Hello. I need business cards designed with our new logo. I'd like to see at least 3 different designs. At least one with a dark background, and at least one with a white background. Maybe one with gray or blue for the background. Play with gradient colors and maybe even insert a pic of a skyline in the background of one or more of them. Use your judgement. We will need 2 cards printed. They need to accommodate the employee name, title, company address, phone, email, and website. Thanks.

Target Market(s)

Wealthy mature investors.

Contact Information for Business Card

Single-sided, professional, clean design that incorporates our logo.

Font styles to use
Sans Serif

Requirements
Must have
• Our new logo needs to be featured on it. (See attached.)
• Employee Name (In all CAPS)
• Title
• Street Address, City, ST Zip Code
• Cell Phone #, Email Address, Website Address
Nice to have
• Design that blends well with our new logo and its colors, or a city scape or other graphic design that looks like an apartment complex in the background. Blues and grays are nice, but use your judgement.
Should not have
• Modern or oriental looking designs or bright colors.

```html
<!DOCTYPE html>
<html lang="en">
<head>
<meta charset="utf-8">
<title>Corvale Holdings Business Card</title>
<link rel="stylesheet" href="https://fonts.googleapis.com/css2?family=Roboto:wght@400;500;700&display=swap">
<style>
  :root {
    --backdrop: #1d1b1a;
    --card: #6a696f;
    --accent: #2ba3e3;
    --ink: #ffffff;
    --rule: rgba(255, 255, 255, 0.45);
  }
  * { margin: 0; padding: 0; box-sizing: border-box; }
  html, body {
    width: 1200px;
    height: 801px;
    overflow: hidden;
    background: var(--backdrop);
    font-family: "Roboto", Arial, sans-serif;
  }
  .card {
    position: absolute;
    left: 100px;
    top: 115px;
    width: 1000px;
    height: 572px;
    background: var(--card);
    color: var(--ink);
  }
  .brand {
    position: absolute;
    left: 95px;
    top: 222px;
    display: flex;
    align-items: center;
    gap: 16px;
  }
  .brand-mark {
    width: 54px;
    height: 54px;
    background: var(--accent);
  }
  .brand-name {
    color: var(--accent);
    font-weight: 500;
    font-size: 30px;
    line-height: 1.05;
    letter-spacing: 1.5px;
    text-transform: uppercase;
  }
  .divider {
    position: absolute;
    left: 478px;
    top: 150px;
    width: 2px;
    height: 280px;
    background: linear-gradient(to bottom, transparent, var(--rule) 30%, var(--rule) 70%, transparent);
  }
  .contact {
    position: absolute;
    left: 530px;
    top: 176px;
  }
  .person-name {
    color: var(--accent);
    font-weight: 700;
    font-size: 34px;
    letter-spacing: 1px;
    text-transform: uppercase;
    line-height: 1.1;
  }
  .person-title {
    font-weight: 500;
    font-size: 23px;
    text-transform: uppercase;
    margin-top: 4px;
    margin-bottom: 18px;
  }
  .address {
    font-style: normal;
    font-size: 22px;
    line-height: 1.35;
    margin-bottom: 16px;
  }
  .channels { list-style: none; }
  .channels li {
    display: flex;
    align-items: center;
    gap: 12px;
    font-size: 22px;
    line-height: 1.4;
    margin-left: -32px;
  }
  .channels svg { width: 20px; height: 20px; fill: var(--accent); flex: none; }
</style>
</head>
<body>
  <main class="card">
    <div class="brand">
      <span class="brand-mark"></span>
      <span class="brand-name">Corvale<br>Holdings, LLC</span>
    </div>

    <div class="divider"></div>

    <section class="contact">
      <h1 class="person-name">Daniel Reyes</h1>
      <p class="person-title">CEO/Founder</p>
      <address class="address">4120 Larchmont Drive<br>Anchorage, Alaska 99508</address>
      <ul class="channels">
        <li>
          <svg viewBox="0 0 24 24" aria-hidden="true"><path d="M6.6 10.8a15.1 15.1 0 0 0 6.6 6.6l2.2-2.2c.3-.3.7-.4 1-.2 1.1.4 2.3.6 3.6.6.6 0 1 .4 1 1V20c0 .6-.4 1-1 1A17 17 0 0 1 3 4c0-.6.4-1 1-1h3.5c.6 0 1 .4 1 1 0 1.3.2 2.5.6 3.6.1.3 0 .7-.2 1z"/></svg>
          <span>907 555 0184</span>
        </li>
        <li>
          <svg viewBox="0 0 24 24" aria-hidden="true"><path d="M2 5h20v14H2z M3.5 6.5 12 12.5l8.5-6" fill="none" stroke="#2ba3e3" stroke-width="0"/><path d="M2 5h20v2l-10 6L2 7z"/><path d="M2 9l10 6 10-6v10H2z"/></svg>
          <span>daniel@corvale.com</span>
        </li>
        <li>
          <svg viewBox="0 0 24 24" aria-hidden="true"><path d="M12 2a10 10 0 1 0 0 20 10 10 0 0 0 0-20zm-1 17.9A8 8 0 0 1 4.2 10L9 14.8v1.1c0 1.1.9 2 2 2zm6.9-2.5c-.3-.8-1-1.4-1.9-1.4h-1v-3c0-.6-.4-1-1-1H8v-2h2c.6 0 1-.4 1-1V7h2c1.1 0 2-.9 2-2v-.4a8 8 0 0 1 2.9 12.8z"/></svg>
          <span>www.corvale.com</span>
        </li>
      </ul>
    </section>
  </main>
</body>
</html>
```